Redesign this Sydney Chocolatier Website

We are looking for a redesign of this websites home page and product pages.

https://marlowconfections.com.au/

Marlow Confections have been making handmade chocolates in Sydney Australia since 1932 they specialize in making hand made chocolates without additives, without palm oil and using all-natural ingredients.

We are looking to rebrand the company to reposition the brand in the high-quality chocolate gifts and hampers market as such they have launched products to tackle this market.

https://marlowconfections.com.au/hampers-2/

Some of the players in this market that we would like to compete with are

https://www.thegiftbasketloft.com.au/

https://www.brintonstreats.com.au/

https://www.chocolate.velqor.com/

The website is currently built on Kova Shop-engine and though it looks decent in our opinion the home page is a little busy and does not convey the quality of the brand.

We are looking for something cleaner that will perform great especially on mobiles.

Target Market(s)

Families and business owners 40+ affluent we specialise in luxury chocolates hampers and chocolate gifts the current look lacks the high end look.

Number of Pages Required

2 page

Font styles to use
Script

Requirements
Must have
• Good SEO Footer, easy to navigate, cleaner than the original design, presents well on mobile devices, plant of room for copy I have included a copy doc with the actual home page copy.
Nice to have
• Something more stylish and high end looking that will appeal to the target market. clean navigation and easy to use that again translates well to mobile, you can use divs and read mores to declutter the long SEO texts see suggested copy doc (you do not have to use all of this
Should not have
• Less cluttered more stylish design than the original website

```html
<!DOCTYPE html>
<html lang="en">
<head>
<meta charset="utf-8">
<title>Marlow Confections — Handmade Chocolates Since 1932</title>
<link href="https://fonts.googleapis.com/css2?family=Pacifico&family=Fira+Sans+Condensed:wght@300;400;500;600&family=Fira+Sans:wght@400;600&display=swap" rel="stylesheet">
<style>
:root{
  --cocoa-dark:#4a2a25;
  --cocoa:#7a4a41;
  --cocoa-tab:#5b3832;
  --mauve:#b9a1a1;
  --text:#5e3c36;
  --grey-bg:#f2f2f2;
  --quote-bg:#f6f3f3;
  --quote-text:#444;
  --white:#fff;
}
*{box-sizing:border-box;margin:0;padding:0}
html,body{width:1200px;height:3502px;overflow:hidden}
body{position:relative;background:var(--white);font-family:"Fira Sans Condensed",sans-serif;color:var(--text)}
.abs{position:absolute}
.script{font-family:"Pacifico",cursive;color:var(--cocoa-dark);font-weight:400}
.btn-dark{position:absolute;background:var(--cocoa-dark);color:var(--white);border-radius:20px;font-size:11px;font-weight:600;display:flex;align-items:center;justify-content:center;letter-spacing:.3px}

/* header */
.site-header{left:0;top:0;width:1200px;height:111px;background:var(--grey-bg)}
.search{left:152px;top:42px;width:186px;height:28px;border:1.5px solid var(--cocoa);border-radius:14px;font-size:12px;padding:0 14px;display:flex;align-items:center;justify-content:space-between;color:var(--cocoa-dark)}
.brand{left:450px;top:34px;width:300px;text-align:center;font-size:24px;font-weight:400;color:var(--cocoa-dark)}
.cart{left:897px;top:41px;width:150px;height:29px;border:1.5px solid var(--cocoa);border-radius:15px;font-size:11px;color:var(--cocoa-dark);display:flex;align-items:center;justify-content:space-between;padding:0 14px}

/* nav */
.main-nav{left:0;top:111px;width:1200px;height:39px;background:var(--cocoa-dark)}
.nav-item{position:absolute;top:0;height:39px;display:flex;align-items:center;justify-content:center;color:var(--white);font-size:12px;font-weight:500;border-right:1px solid #6a4a44}
.nav-item.active{background:var(--cocoa-tab)}
.dropdown{left:650px;top:150px;width:161px;height:172px;background:var(--white);padding:18px 20px}
.dropdown a{display:block;font-size:10.5px;font-weight:500;color:var(--cocoa-dark);text-decoration:none;margin-bottom:22px;position:relative}
.dropdown a::after{content:"";position:absolute;left:0;top:17px;width:36px;height:2px;background:var(--mauve)}

/* hero */
.hero{left:0;top:150px;width:1200px;height:373px;background:linear-gradient(100deg,#d9c8bf 0%,#a7807a 35%,#c89a8f 60%,#6b4a3e 100%)}
.hero-title{left:0;top:235px;width:1200px;text-align:center;font-family:"Pacifico",cursive;color:var(--white);font-size:44px;line-height:56px}

/* story */
.story-photo{left:280px;top:584px;width:284px;height:424px;background:linear-gradient(160deg,#e9e3de,#6b4a3a 60%,#3a241c)}
.story-card{left:544px;top:722px;width:375px;height:372px;background:var(--white);box-shadow:0 2px 8px rgba(0,0,0,.18);padding:54px 30px 0}
.story-title{left:544px;top:694px;width:375px;text-align:center;font-size:28px}
.story-mark{left:544px;top:820px;width:375px;text-align:center;font-family:"Fira Sans Condensed",sans-serif;font-weight:600;font-size:80px;line-height:86px;color:rgba(120,80,70,.09)}
.story-card p{font-size:14px;line-height:27px;text-align:center;font-weight:300;position:relative}

.rule{left:150px;top:1140px;width:900px;height:1px;background:#888}
.col-rule{left:600px;top:1186px;width:1px;height:377px;background:#ccc}
.col-title{font-size:28px;text-align:center}
.col-text{font-size:14px;line-height:27px;font-weight:300;color:var(--cocoa-dark)}
.learn{left:978px;top:1535px;font-size:14px;font-weight:500;color:var(--cocoa-dark);border-bottom:3px solid var(--mauve);line-height:18px}

/* products */
.section-title{left:0;width:1200px;text-align:center;font-size:28px}
.product-card{top:1680px;width:292px;height:148px;background:var(--cocoa);color:var(--white)}
.product-card h3{position:absolute;font-size:17px;font-weight:500}
.product-card p{position:absolute;font-size:11px;line-height:14px;font-weight:300}
.product-card svg{position:absolute}
.view-btn{top:1814px;width:147px;height:34px;background:var(--white);border:2px solid var(--cocoa);border-radius:17px;font-size:11px;font-weight:500;color:var(--cocoa-dark);display:flex;align-items:center;justify-content:center}

.cat-img{top:1971px;width:208px;height:209px;box-shadow:1px 1px 4px rgba(0,0,0,.2)}
.cat-label{top:2196px;width:208px;text-align:center;font-size:18px;font-weight:500;color:var(--cocoa)}

/* occasion banner */
.occasion-left{left:0;top:2260px;width:600px;height:374px;background:linear-gradient(135deg,#b89a93,#8e6a62 60%,#b89d96)}
.occasion-right{left:600px;top:2260px;width:600px;height:374px;background:linear-gradient(135deg,#7a5047,#a27c72 55%,#c2aaa3)}
.occasion-text{left:0;top:2366px;width:1200px;text-align:center;color:var(--white);font-size:25px;line-height:33px;font-weight:500}

/* testimonials */
.quote-box{left:188px;top:2736px;width:824px;height:342px;background:var(--quote-bg);text-align:center;font-family:"Fira Sans",sans-serif;color:var(--quote-text)}
.quote-mark{position:absolute;left:0;top:20px;width:824px;font-family:"Fira Sans",sans-serif;font-weight:600;font-style:italic;font-size:64px;color:var(--cocoa-dark)}
.quote-body{position:absolute;left:30px;top:88px;width:764px;font-size:16px;line-height:21.5px}
.quote-name{position:absolute;left:0;top:288px;width:790px;font-size:16px;font-weight:600;color:#333}
.arrow{width:22px;height:22px}

/* delivery strip */
.delivery{left:0;top:3123px;width:1200px;height:71px;background:var(--mauve)}
.delivery-head{left:300px;top:3134px;width:340px;text-align:center;font-family:"Fira Sans",sans-serif;font-weight:600;font-size:16px;color:var(--cocoa-dark)}
.delivery-sub{left:300px;top:3158px;width:340px;text-align:center;font-family:"Fira Sans",sans-serif;font-size:12px;color:var(--cocoa-dark)}

/* footer */
.site-footer{left:0;top:3194px;width:1200px;height:308px;background:var(--cocoa-dark);color:var(--white)}
.foot-label{font-size:13px;font-weight:600;color:var(--white)}
.foot-small{font-size:11px;line-height:14px;color:var(--white);font-weight:300}
.foot-link{font-size:12px;color:var(--white);font-weight:300}
.news-input{left:787px;top:3304px;width:186px;height:29px;background:var(--white);font-size:11px;color:#555;display:flex;align-items:center;padding-left:14px}
.news-btn{left:973px;top:3304px;width:75px;height:29px;background:var(--mauve);font-size:11px;font-weight:600;color:var(--cocoa-dark);display:flex;align-items:center;justify-content:center}
.foot-rule{left:150px;top:3433px;width:900px;height:1px;background:#6e4d47}
.social{top:3455px;width:22px;height:22px;border:1.5px solid var(--white);border-radius:4px}
</style>
</head>
<body>

<header class="site-header abs">
  <div class="search abs"><span>Search</span>
    <svg width="14" height="14" viewBox="0 0 14 14"><circle cx="5.5" cy="5.5" r="4.3" fill="none" stroke="#4a2a25" stroke-width="1.8"/><line x1="8.6" y1="8.6" x2="13" y2="13" stroke="#4a2a25" stroke-width="2"/></svg>
  </div>
  <div class="brand abs">Marlow Confections</div>
  <div class="cart abs"><span>0 item(s) - $0.00</span>
    <svg width="14" height="13" viewBox="0 0 14 13"><path d="M0 1h2.5l2 7h7l2-5H4" fill="none" stroke="#4a2a25" stroke-width="1.6"/><circle cx="5.5" cy="11" r="1.3" fill="#4a2a25"/><circle cx="10.5" cy="11" r="1.3" fill="#4a2a25"/></svg>
  </div>
</header>

<nav class="main-nav abs">
  <div class="nav-item active" style="left:253px;width:104px;border-left:1px solid #6a4a44">HOME</div>
  <div class="nav-item" style="left:357px;width:141px">CHOCOLATES</div>
  <div class="nav-item" style="left:498px;width:152px">SPECIAL EVENTS</div>
  <div class="nav-item active" style="left:650px;width:161px">GIFTS &amp; HAMPERS</div>
  <div class="nav-item" style="left:811px;width:133px">CONTACT US</div>
</nav>

<section class="hero abs" role="img" aria-label="Photo of a chocolatier drizzling melted chocolate over handmade chocolates"></section>
<div class="dropdown abs">
  <a>HAMPERS</a><a>GIFTS &amp; HAMPERS</a><a>SNACK BAGS</a><a>CORPORATE &amp; PREMIUM</a>
</div>
<h1 class="hero-title abs">Taste the great<br>homemade chocolate</h1>
<div class="btn-dark" style="left:507px;top:391px;width:186px;height:34px">SHOP NOW</div>

<section>
  <div class="story-photo abs" role="img" aria-label="Photo of hands decorating rows of chocolate truffles on a tray"></div>
  <div class="story-card abs">
    <p>Marlow Confections was founded by Arthur Marlow in 1932. Arthur had a passion for making handmade chocolate from his kitchen in Paddington. In time, he became a master at his craft and developed a loyal customer following. From his efforts, some of Australia's most delicious fondants, hard centres, jellies and gingers coated with the finest chocolate were conceived. Arthur is no longer with us, but his passion for fine handmade chocolates and the original recipes on which the Marlow' brand was built endure.</p>
  </div>
  <div class="story-mark abs">SINCE<br>1932</div>
  <h2 class="story-title script abs">Our Story</h2>
</section>

<div class="rule abs"></div>
<div class="col-rule abs"></div>

<h2 class="col-title script abs" style="left:150px;top:1193px;width:410px">Gluten free chocolates</h2>
<p class="col-text abs" style="left:154px;top:1277px;width:416px">In recent year, many customers began asking us to cater for chocolate lovers who are gluten intolerant. Through expirementation, we are happy to say that we met the request. We sprinke wheat four instead of just flour to keep the newly formed chocolate centres from sticking to the trays. Thus, we were able to produce delicious, gluten-free chocolates.<br><br>Even with this process, the same great chocolate taste we've become famous for hasn't changed! Our hand-made chocolates are still faithful to the original recipe, and they're delicious!</p>

<h2 class="col-title script abs" style="left:630px;top:1193px;width:420px">Handmade without palm oil</h2>
<p class="col-text abs" style="left:637px;top:1277px;width:418px">Our hand-crafted chocolates are also palm oil free! Marlow hand-made chocolates are made with cocoa powder and cocoa butter. They are not made with vegetable oil.<br><br>A few years ago, Marlow was using comppound chocolate which contains palm oil. We experimented a lot with our recipe to get the balance right and retain the classic Marlow taste our customers love. By successfully replacing palm oil, we dramatically reduced our environmental impact and, and happily, improved the quality of our product to boot!</p>
<div class="learn abs">Learn more</div>

<h2 class="section-title script abs" style="top:1612px">Our Products</h2>

<div class="product-card abs" style="left:151px">
  <svg style="left:14px;top:28px" width="56" height="72" viewBox="0 0 56 72" fill="none" stroke="#fff" stroke-width="2"><rect x="4" y="2" width="40" height="62"/><rect x="10" y="8" width="12" height="14"/><rect x="26" y="8" width="12" height="14"/><rect x="10" y="26" width="12" height="14"/><rect x="26" y="26" width="12" height="14"/><path d="M2 44l52 26M2 44v26h52"/></svg>
  <h3 style="left:93px;top:12px">Our Chocolates</h3>
  <p style="left:93px;top:40px;width:192px">Delicious chocolates in a great variety of flavours, handmade to perfection in our Sydney factory, and delivered to your door throughout Australia. Discover Marlow today!</p>
</div>
<div class="product-card abs" style="left:453px">
  <svg style="left:14px;top:26px" width="74" height="74" viewBox="0 0 74 74" fill="none" stroke="#fff" stroke-width="2"><rect x="6" y="24" width="62" height="14"/><rect x="10" y="38" width="54" height="34"/><line x1="37" y1="24" x2="37" y2="72"/><path d="M37 24c-8-16-22-16-20-6 2 6 20 6 20 6zM37 24c8-16 22-16 20-6-2 6-20 6-20 6z"/></svg>
  <h3 style="left:115px;top:12px">Gifts &amp; Hampers</h3>
  <p style="left:115px;top:40px;width:170px">As with all our chocolates, our hampers are handmade with care from our Kingsgrove shop and hand-wrapped and styled to suit the occasion.</p>
</div>
<div class="product-card abs" style="left:756px">
  <svg style="left:14px;top:36px" width="74" height="62" viewBox="0 0 74 62" fill="none" stroke="#fff" stroke-width="2"><path d="M46 34S30 22 30 12c0-6 8-10 16-2 8-8 16-4 16 2 0 10-16 22-16 22z"/><circle cx="41" cy="14" r="1" fill="#fff"/><circle cx="51" cy="14" r="1" fill="#fff"/><path d="M42 20q4 3 8 0"/><path d="M2 40h10v18H2zM12 42h16l12 4h20l6 4-6 4H40M12 56h40l20-14"/></svg>
  <h3 style="left:101px;top:20px">Corporate &amp; Personalised</h3>
  <p style="left:101px;top:50px;width:180px">Give a very special and memorable gift to partners, clients and prospects with branded packaging and personalised cards</p>
</div>
<div class="view-btn abs" style="left:221px">View Products</div>
<div class="view-btn abs" style="left:522px">View Products</div>
<div class="view-btn abs" style="left:826px">View Products</div>

<h2 class="section-title script abs" style="top:1885px">Featured Categories</h2>
<div class="cat-img abs" style="left:154px;background:radial-gradient(circle,#6a2a22 0%,#3e2019 45%,#fafafa 75%)" role="img" aria-label="Photo of boxed dark chocolates tied with red ribbon"></div>
<div class="cat-img abs" style="left:385px;background:radial-gradient(circle,#7a3a2c 0%,#4a2a22 45%,#fafafa 75%)" role="img" aria-label="Photo of boxed milk chocolates tied with red ribbon"></div>
<div class="cat-img abs" style="left:616px;background:radial-gradient(circle,#4a2a20 0%,#5a3526 38%,#fff 60%)" role="img" aria-label="Photo of soft centre chocolates, one cut open"></div>
<div class="cat-img abs" style="left:833px;background:radial-gradient(circle,#6a4530 0%,#b8a05a 45%,#fff 72%)" role="img" aria-label="Photo of a box of hard centre chocolates"></div>
<div class="cat-label abs" style="left:154px">Dark Chocolates</div>
<div class="cat-label abs" style="left:397px">Milk Chocolates</div>
<div class="cat-label abs" style="left:616px">Soft Centres</div>
<div class="cat-label abs" style="left:847px">Hard Chocolates</div>

<div class="occasion-left abs" role="img" aria-label="Photo of an open gift box of assorted chocolates"></div>
<div class="occasion-right abs" role="img" aria-label="Photo of assorted chocolates and truffles"></div>
<p class="occasion-text abs">Holidays, birthdays, anniversaries.<br>No matter what you're celebrating, you'll find in our handmade<br>chocolates the perfect gift for any occasion.</p>
<div class="btn-dark" style="left:492px;top:2488px;width:186px;height:34px">SHOP NOW</div>

<h2 class="section-title script abs" style="top:2668px">Testimonials</h2>
<div class="quote-box abs">
  <div class="quote-mark">&ldquo;</div>
  <p class="quote-body">Hi Ruth and Colin<br>Many thanks for the years of providing wonderful chocolates.<br>You supplied myself personally and our business when we had a hotel at Kogarah and a bottle shop at Loftus.<br><br>I have had the pleasure of dealing with your company since 1984 and have always been treated with wonderful service<br>And great quality of chocolate products. Some of your products we are unable to purchase from other stores because they are unique to your company.</p>
  <p class="quote-name">Dana Whitfield</p>
</div>
<svg class="arrow abs" style="left:152px;top:2896px" viewBox="0 0 22 22"><circle cx="11" cy="11" r="11" fill="#4a2a25"/><path d="M13 6l-5 5 5 5" fill="none" stroke="#fff" stroke-width="2"/></svg>
<svg class="arrow abs" style="left:1025px;top:2896px" viewBox="0 0 22 22"><circle cx="11" cy="11" r="11" fill="#4a2a25"/><path d="M9 6l5 5-5 5" fill="none" stroke="#fff" stroke-width="2"/></svg>

<div class="delivery abs"></div>
<div class="delivery-head abs">We deliver rain or shine!</div>
<div class="delivery-sub abs">Free shipping for any order over $35</div>
<div class="btn-dark" style="left:661px;top:3142px;width:187px;height:35px">SHOP NOW</div>

<footer class="site-footer abs"></footer>
<svg class="abs" style="left:156px;top:3240px" width="16" height="22" viewBox="0 0 16 22" fill="none" stroke="#fff" stroke-width="1.5"><path d="M8 21S1 12 1 8a7 7 0 0 1 14 0c0 4-7 13-7 13z"/><circle cx="8" cy="8" r="2.5"/></svg>
<div class="foot-label abs" style="left:188px;top:3240px">Address</div>
<div class="foot-small abs" style="left:188px;top:3258px;width:160px">Lorem ipsum dolor sit amet, consectetur adipiscing elit, sed</div>
<svg class="abs" style="left:151px;top:3303px" width="22" height="22" viewBox="0 0 22 22" fill="none" stroke="#fff" stroke-width="1.5"><path d="M5 1l4 5-2 3c1 3 3 5 6 6l3-2 5 4-3 4C9 20 2 13 1 4z"/></svg>
<div class="foot-label abs" style="left:188px;top:3301px">Phone</div>
<div class="foot-small abs" style="left:188px;top:3319px">+61 2 9000 4417</div>
<svg class="abs" style="left:153px;top:3345px" width="20" height="20" viewBox="0 0 20 20" fill="none" stroke="#fff" stroke-width="1.5"><path d="M1 8l9-7 9 7v11H1z"/><path d="M1 8l9 6 9-6"/><rect x="5" y="4" width="10" height="7"/></svg>
<div class="foot-label abs" style="left:188px;top:3343px">Email</div>
<div class="foot-small abs" style="left:188px;top:3361px">hello@marlowconfections.com.au</div>

<div class="foot-label abs" style="left:497px;top:3244px">Quick links</div>
<div class="foot-link abs" style="left:497px;top:3280px">Recipes</div>
<div class="foot-link abs" style="left:497px;top:3310px">Terms and Conditions</div>
<div class="foot-link abs" style="left:497px;top:3340px">Private Policy</div>
<div class="foot-link abs" style="left:497px;top:3370px">Shipping Policy</div>

<div class="foot-label abs" style="left:787px;top:3253px">Subscribe to our Newsletter</div>
<div class="foot-small abs" style="left:787px;top:3281px;font-size:12px">Don't miss out on our special offers!</div>
<div class="news-input abs">Enter email address</div>
<div class="news-btn abs">SUBMIT</div>

<div class="foot-rule abs"></div>
<div class="foot-small abs" style="left:152px;top:3460px;font-size:12px">© 2020 Marlow Confections. All Rights Reserved.</div>
<div class="social abs" style="left:880px"></div>
<div class="social abs" style="left:917px"></div>
<div class="social abs" style="left:955px"></div>
<div class="social abs" style="left:992px"></div>
<div class="social abs" style="left:1028px"></div>

</body>
</html>
```